Ember Roastery specialty coffee shop business card

Please use Design #4817053 from previous project (logo design). Ember Roastery is a new coffee shop that will serve specialty coffee and will focus on high quality products. I would like to use orange and brown colors. I like designs that are simple but elegant and that deliver a message that is easy to recognize. I will upload a file of the logo design.

Industry/Entity Type

Coffee Shop

Contact Information for Business Card

Marin Vantadesh
(415) 555-0172

Font styles to use
Serif
Sans Serif
Script

Requirements
Must have
• simple and elegant, colors match nicely, I like to use orange and brown. Background creme color.
Should not have
• complex designs that are hard to understand.

```html
<!DOCTYPE html>
<html lang="en">
<head>
<meta charset="utf-8">
<title>Ember Roastery – Business Card</title>
<link rel="stylesheet" href="https://fonts.googleapis.com/css2?family=Tinos:ital,wght@1,400&display=swap">
<style>
  :root {
    --creme: #f0d8c8;
    --espresso: #3a1f10;
    --roast: #6b3a12;
    --caramel: #c49a5c;
    --foam: #f0d8c8;
  }
  html, body {
    margin: 0;
    padding: 0;
    width: 686px;
    height: 1200px;
    overflow: hidden;
    background: var(--creme);
  }
  .card {
    position: relative;
    width: 686px;
    height: 1200px;
    background: var(--creme);
    font-family: "Tinos", "Times New Roman", serif;
    font-style: italic;
    font-weight: 400;
  }
  .brand {
    position: absolute;
    top: 0;
    left: 0;
    width: 686px;
    height: 660px;
    display: flex;
    align-items: center;
    justify-content: center;
    gap: 22px;
  }
  .brand-dot {
    width: 48px;
    height: 48px;
    border-radius: 50%;
    background: var(--caramel);
    flex: none;
  }
  .brand-name {
    margin: 0;
    font-size: 84px;
    line-height: 1;
    color: var(--espresso);
    font-weight: 400;
    white-space: nowrap;
  }
  .holder {
    position: absolute;
    top: 834px;
    left: 0;
    width: 686px;
    margin: 0;
    text-align: center;
    color: var(--roast);
    font-size: 86px;
    line-height: 86px;
    font-weight: 400;
  }
  .holder span { display: block; }
  .contact-band {
    position: absolute;
    left: 0;
    bottom: 0;
    width: 686px;
    height: 172px;
    background: var(--espresso);
    display: flex;
    align-items: center;
    justify-content: center;
  }
  .phone {
    margin: 0;
    color: var(--foam);
    font-size: 66px;
    letter-spacing: 1px;
  }
</style>
</head>
<body>
  <main class="card">
    <header class="brand">
      <span class="brand-dot" aria-hidden="true"></span>
      <h1 class="brand-name">Ember Roastery</h1>
    </header>

    <h2 class="holder">
      <span class="holder-first">Marin</span>
      <span class="holder-last">Vantadesh</span>
    </h2>

    <footer class="contact-band">
      <p class="phone">415.555.0172</p>
    </footer>
  </main>
</body>
</html>
```